Disability and mental health support work company requires business card

Specialising
Bellwind Disability is a new HVTA service aimed toward HVTA participants with a history of criminal justice, psychosocial/mental health, intellectual, and cognitive disabilities.

Our focus
Focusing on providing core HVTA supports for community participation, daily activities and supported independent living.

Authentic
Likeminded people wanting to make a difference in participant's lives.

Our aim to provide holistic and empowering supports targeted towards creating independence and guidance for all participants and families.
Over 35 years of experience working with people that have psychosocial, intellectual, and cognitive disabilities.

Industry/Entity Type

disability and mental health

Contact Information for Business Card

logo - business name

Colors
0054AA
0677BA
7BADD7
CADEEF
E8F1F8
FFF300
FFF600
FEFA6F
FFFEC7
FFFEE8

Requirements
Must have
• want double sided business cards(wont let me change it)
Should not have
• any disability related pictures

```html
<!DOCTYPE html>
<html lang="en">
<head>
<meta charset="utf-8">
<title>Bellwind Disability – Business Card</title>
<link rel="stylesheet" href="https://fonts.googleapis.com/css2?family=Open+Sans:wght@400;600;700&display=swap">
<style>
  :root {
    --backdrop: #8f9ba7;
    --card-navy: #13385f;
    --card-navy-pattern: #173f69;
    --accent-gold: #f2b51c;
    --accent-sky: #8ec0ea;
    --text-white: #ffffff;
  }
  * { box-sizing: border-box; margin: 0; padding: 0; }
  html, body {
    width: 1200px; height: 780px; overflow: hidden;
    background: var(--backdrop);
    font-family: "Open Sans", sans-serif;
  }
  .canvas {
    position: relative; width: 1200px; height: 780px;
    display: flex; flex-direction: column; align-items: center; justify-content: center; gap: 30px;
  }
  .card {
    position: relative; width: 600px; height: 343px;
    background: var(--card-navy);
    box-shadow: 0 6px 16px rgba(0,0,0,0.35);
    overflow: hidden;
  }
  /* back side */
  .card-back__pattern {
    position: absolute; inset: 0;
    background: radial-gradient(circle at 50% 50%, var(--card-navy) 20%, var(--card-navy-pattern) 100%);
  }
  .brand-mark {
    position: absolute; display: flex; align-items: center; gap: 10px;
    color: var(--accent-sky); font-weight: 600; letter-spacing: 0.12em; text-transform: uppercase;
  }
  .brand-mark__dot {
    border: 2px solid var(--accent-sky); border-radius: 50%;
  }
  .card-back .brand-mark {
    left: 50%; top: 50%; transform: translate(-50%, -50%);
    font-size: 22px;
  }
  .card-back .brand-mark__dot { width: 22px; height: 22px; }
  /* front side */
  .card-front .brand-mark {
    right: 34px; top: 40px; font-size: 13px; gap: 8px;
  }
  .card-front .brand-mark__dot { width: 14px; height: 14px; border-width: 1.5px; }
  .holder {
    position: absolute; left: 40px; top: 168px;
  }
  .holder__name {
    color: var(--accent-gold); font-weight: 700; font-size: 34px; line-height: 1; letter-spacing: -0.01em;
  }
  .holder__title {
    color: var(--text-white); font-size: 10.5px; font-weight: 400; margin-top: 4px; letter-spacing: 0.01em;
  }
  .divider {
    position: absolute; left: 40px; right: 40px; top: 232px;
    height: 1px; background: var(--accent-gold);
  }
  .contact-list {
    position: absolute; left: 52px; top: 244px; list-style: none;
  }
  .contact-list li {
    display: flex; align-items: center; gap: 7px;
    color: var(--text-white); font-size: 13px; line-height: 20px;
  }
  .contact-list svg { width: 11px; height: 11px; fill: var(--accent-gold); flex: none; }
  .address {
    position: absolute; right: 40px; top: 246px; text-align: right;
    color: var(--accent-gold); font-weight: 600; font-size: 12.5px; line-height: 17px;
  }
</style>
</head>
<body>
<main class="canvas">

  <section class="card card-back" aria-label="Business card back">
    <div class="card-back__pattern" role="img" aria-label="Faint repeating pattern of the company emblem across the card"></div>
    <div class="brand-mark">
      <span class="brand-mark__dot"></span>
      <span class="brand-mark__name">Bellwind Disability</span>
    </div>
  </section>

  <section class="card card-front" aria-label="Business card front">
    <div class="brand-mark">
      <span class="brand-mark__dot"></span>
      <span class="brand-mark__name">Bellwind Disability</span>
    </div>

    <div class="holder">
      <h1 class="holder__name">MARCUS HALE</h1>
      <p class="holder__title">MANAGING DIRECTOR</p>
    </div>

    <div class="divider"></div>

    <ul class="contact-list">
      <li>
        <svg viewBox="0 0 24 24" aria-hidden="true"><path d="M6.6 10.8a15.1 15.1 0 0 0 6.6 6.6l2.2-2.2a1 1 0 0 1 1-.25 11.4 11.4 0 0 0 3.6.57 1 1 0 0 1 1 1V20a1 1 0 0 1-1 1A17 17 0 0 1 3 4a1 1 0 0 1 1-1h3.5a1 1 0 0 1 1 1c0 1.25.2 2.45.57 3.57a1 1 0 0 1-.25 1z"/></svg>
        <span>+1 555 014 2290</span>
      </li>
      <li>
        <svg viewBox="0 0 24 24" aria-hidden="true"><path d="M2 5h20v14H2z M2 5l10 8 10-8" fill="none" stroke="#f2b51c" stroke-width="2.5"/></svg>
        <span>hello@bellwind.com</span>
      </li>
      <li>
        <svg viewBox="0 0 24 24" aria-hidden="true"><circle cx="12" cy="12" r="10" fill="none" stroke="#f2b51c" stroke-width="2"/><path d="M2 12h20M12 2c3 3 3 17 0 20M12 2c-3 3-3 17 0 20" fill="none" stroke="#f2b51c" stroke-width="1.6"/></svg>
        <span>www.bellwinddisability.com</span>
      </li>
    </ul>

    <address class="address" style="font-style:normal">
      41 #118, Fairhaven<br>
      Maine 04021, United States
    </address>
  </section>

</main>
</body>
</html>
```